Veranstaltungsservice für Firmenfeste sucht Logo & Visitenkarte
Zielgruppe
Zielgruppe: Firmen
Wir sind ein veranstaltungsservice für Firmenfeste. Wir haben das Equipment von A bis Z. Hierbei geht es nicht rein nur, um das Equipment von einem Event sondern auch um aktivitäten ( ab 3 Jahre bis 99Jahre). Wir liefern, bauen auf, moderrieren durchs Programm und orgranisieren Abbau und den Rücktransport. Es wäre sinnvoll wenn Sie sich unseren Image Film anschauen, da erfahren Sie sehr viel über uns.
Wir möchten nochmal deutlich drauf hinweissen, dass es in Zukunft mehr in richtung Erwachsene gehen soll, anstatt Kinder. Allerdings werden wir den Nachwuchs nicht vernachlässigen.
Link für HP und Image film: https://www.festhalmwiese.example/home/
Aufgabenstellung
- Gerne in einer Form wie z.B in einem Kreis oder ähnlichem. Die gefielen uns auch in den Vorschlägen gut
- Soll nicht verspielt aussehen
- Wir wollen in Zukunft vorallem Erwachsene ansprechen und Aktivitäten mit ihnen durchführen. Wobei wir den Nachwuchs nicht vernachlässigen werden!
- Gerne eine Kreative aber gut Lesbare Schriftart
- Da blau unser Firmenfarbe ist, sollte es berücksichtigt werden.
- Wir haben die Rot tönne mit ausgewählt, da diese für aktivität stehen
- Wenn man unser Ziel reinbringen könnte wäre es wünschenswert: Mitarbeiter sollen lange von dem Fest reden. Dadurch soll eine Motivation des Teams entstehen, wovon die Arbeitgeben provitieren.
- Gerne auch Bilder von Hauptatraktionen wie das beleuchtete zelt. ( Kein Muss!!!!!)
Wir hoffen auf Ihre Ideen und Vorschläge.

```html
<!DOCTYPE html>
<html lang="de">
<head>
<meta charset="utf-8">
<title>Visitenkarte – Rückseite</title>
<link rel="stylesheet" href="https://fonts.googleapis.com/css2?family=Mulish:wght@300;400&display=swap">
<style>
  :root {
    --navy: #1b3556;
    --red: #c4253f;
    --paper: #ffffff;
  }
  html, body {
    margin: 0;
    padding: 0;
    width: 1200px;
    height: 667px;
    overflow: hidden;
    background: var(--paper);
  }
  .card {
    position: relative;
    width: 1200px;
    height: 667px;
    background: var(--paper);
    font-family: "Mulish", sans-serif;
    font-style: normal;
    color: var(--navy);
  }
  .brand {
    position: absolute;
    left: 40px;
    top: 190px;
    width: 580px;
    display: flex;
    align-items: center;
    justify-content: center;
    gap: 22px;
  }
  .brand__dot {
    width: 26px;
    height: 26px;
    border-radius: 50%;
    background: var(--red);
    flex: none;
  }
  .brand__name {
    margin: 0;
    font-weight: 300;
    font-size: 66px;
    line-height: 1;
    letter-spacing: 1px;
    color: var(--navy);
    white-space: nowrap;
  }
  .contact {
    position: absolute;
    left: 618px;
    top: 362px;
    font-style: normal;
    font-weight: 300;
    font-size: 34px;
    line-height: 52px;
    white-space: nowrap;
  }
  .contact__group {
    margin: 0 0 28px;
  }
</style>
</head>
<body>
  <main class="card">
    <div class="brand">
      <span class="brand__dot"></span>
      <h1 class="brand__name">Festhalmwiese</h1>
    </div>
    <address class="contact">
      <p class="contact__group">Am Festanger 7<br>53947 Wiesental-Halmbach</p>
      <p class="contact__group">Tel: 02461-578<br>Mail: info@festhalmwiese.example</p>
    </address>
  </main>
</body>
</html>
```